Flyer design for the Harvest Lantern Summit 2019 (HALSUM)

Design a flyer for our annual conference with basic information about the conference: conference logo and year, Conference name: Harvest Lantern Summit Location: Talbot Community Center (Downtown Portland)482 Wexley Street, Portland, ME 04109, Date: August 8th, 9th, 10th and 11th, 2019Start time 7:00PMI would like the following three words added to the flyer. These words describe the vision of the conference: Prophetic, Fire, Overflow,

Contact info:
Website: www.vostel.org
Phone: 207 555 3184
Email: contact@meadowcrest.org

Target Market(s)

Young adults living in the United States

Industry/Entity Type

Religious

Font styles to use
Sans Serif

Colors

Designer to choose colors to be used in the design.

Requirements
Must have
• HALSUM must logo standout, the reader should be able to take a quick look and find key info,
Should not have
• Cross image, church image

```html
<!DOCTYPE html>
<html lang="en">
<head>
<meta charset="utf-8">
<title>Harvest Lantern Summit 2019 – Flyer Concepts</title>
<link rel="stylesheet" href="https://fonts.googleapis.com/css2?family=Montserrat:wght@400;600;700;800;900&display=swap">
<style>
:root{
  --orange:#f7941d;
  --orange-deep:#f26b1d;
  --orange-soft:#fbb040;
  --blue:#1c75bc;
  --navy:#16325c;
  --ink:#1a1a1a;
  --white:#ffffff;
  --sheet:#ececec;
  --grey:#5a5a5a;
}
*{box-sizing:border-box;margin:0;padding:0}
html,body{width:872px;height:1200px;overflow:hidden;background:var(--sheet)}
body{font-family:'Montserrat',sans-serif;color:var(--ink)}
.sheet{position:relative;width:872px;height:1200px;background:var(--sheet)}

.flyer{position:absolute;width:366px;height:500px;overflow:hidden;display:flex;flex-direction:column;align-items:center;background:var(--white);box-shadow:0 2px 6px rgba(0,0,0,.18)}
.flyer--one{left:52px;top:48px;background:linear-gradient(160deg,var(--white) 0%,var(--white) 38%,var(--orange-soft) 62%,var(--orange) 100%)}
.flyer--two{left:454px;top:48px}
.flyer--three{left:52px;top:618px;background:linear-gradient(180deg,var(--white) 0 74px,var(--orange) 74px,var(--orange-deep) 55%,var(--blue) 100%)}
.flyer--four{left:454px;top:618px;background:linear-gradient(180deg,var(--white) 0 74px,var(--orange) 74px,var(--orange-deep) 100%)}

.swoosh{position:absolute;right:-40px;top:150px;width:260px;height:260px;border-radius:50%;background:radial-gradient(circle,rgba(255,255,255,.35),rgba(255,255,255,0) 70%)}

.brand{display:flex;flex-direction:column;align-items:center;line-height:1}
.brand-name{display:flex;align-items:center;gap:6px;font-weight:800;font-size:30px;letter-spacing:1px;color:var(--orange)}
.brand-dot{width:14px;height:14px;border-radius:50%;background:var(--orange)}
.brand-year{font-weight:700;font-size:11px;letter-spacing:4px;color:var(--blue);margin-top:3px}
.brand--top{height:74px;justify-content:center;width:100%}

.title{display:flex;flex-direction:column;align-items:center;line-height:1;text-transform:uppercase;width:100%}
.title-lead{font-weight:800;font-size:22px;letter-spacing:1px}
.title-main{font-weight:900;font-size:60px;letter-spacing:1px;margin-top:2px}
.title-tail{font-weight:600;font-size:22px;letter-spacing:6px;margin-top:2px}
.title--orange{color:var(--orange);padding-top:30px}
.title--blue-block{background:var(--blue);color:var(--white);padding:14px 0 12px}
.title--white{color:var(--white);padding-top:16px}

.vision{width:100%;text-align:center;font-weight:700;font-size:16px;letter-spacing:1px;padding:7px 0;margin-top:10px}
.vision--blue{background:var(--blue);color:var(--white)}
.vision--plain{color:var(--blue);margin-top:0;background:var(--white)}
.vision--dark{background:var(--ink);color:var(--white)}

.date{margin-top:14px;text-align:center;line-height:1.15}
.date-label{font-size:9px;font-weight:600;color:var(--grey)}
.date-range{font-weight:800;font-size:22px;color:var(--navy)}
.date-time{font-size:9px;font-weight:600;color:var(--grey)}
.date-time strong{font-size:13px;color:var(--navy)}
.date--card{background:var(--white);padding:8px 22px;border-radius:3px}

.venue{margin-top:12px;text-align:center;line-height:1.25}
.venue-label{font-size:8px;font-weight:600}
.venue-text{font-size:11px;font-weight:700}
.venue--dark{color:var(--navy)}
.venue--light{color:var(--white)}

.brand--bottom{margin-top:auto;margin-bottom:10px}
.brand--bottom-light .brand-name{color:var(--white)}
.brand--bottom-light .brand-dot{background:var(--white)}
.brand--bottom-light .brand-year{color:var(--navy)}

.contacts{width:100%;height:22px;display:flex;justify-content:space-around;align-items:center;font-size:6.5px;font-weight:600;text-transform:uppercase}
.contacts--light{background:var(--white);color:var(--orange-deep)}
.contacts--dark{background:var(--ink);color:var(--white);margin-top:auto}
.contact{display:flex;align-items:center;gap:3px}
.contact-icon{width:8px;height:8px;border-radius:50%;background:var(--orange)}

.sample-label{position:absolute;font-size:11px;color:var(--grey)}
.sheet-caption{position:absolute;left:0;width:872px;top:1160px;text-align:center;font-size:12px;color:var(--grey)}
</style>
</head>
<body>
<main class="sheet">

  <section class="flyer flyer--one">
    <div class="swoosh" role="img" aria-label="Soft white flame-like swoosh decoration"></div>
    <div class="title title--orange">
      <span class="title-lead">Harvest</span>
      <span class="title-main">Lantern</span>
      <span class="title-tail">Summit</span>
    </div>
    <div class="vision vision--blue">PROPHETIC | FIRE | OVERFLOW</div>
    <div class="date date--card">
      <div class="date-label">Date on</div>
      <div class="date-range">AUGUST 8TH - 11TH 2019</div>
      <div class="date-time">Start time <strong>7:00PM</strong></div>
    </div>
    <div class="venue venue--dark">
      <div class="venue-label">Location at</div>
      <div class="venue-text">Talbot Community Center<br>(Downtown Portland) 482 Wexley Street,<br>Portland, ME 04109</div>
    </div>
    <div class="brand brand--bottom brand--bottom-light">
      <span class="brand-name"><span class="brand-dot"></span>HALSUM</span>
      <span class="brand-year">2019</span>
    </div>
    <div class="contacts contacts--light">
      <span class="contact"><span class="contact-icon"></span>www.vostel.org</span>
      <span class="contact"><span class="contact-icon"></span>207 555 3184</span>
      <span class="contact"><span class="contact-icon"></span>contact@meadowcrest.org</span>
    </div>
  </section>

  <section class="flyer flyer--two">
    <div class="brand brand--top">
      <span class="brand-name"><span class="brand-dot"></span>HALSUM</span>
      <span class="brand-year">2019</span>
    </div>
    <div class="title title--blue-block">
      <span class="title-lead">Harvest</span>
      <span class="title-main">Lantern</span>
      <span class="title-tail">Summit</span>
    </div>
    <div class="vision vision--plain">PROPHETIC | FIRE | OVERFLOW</div>
    <div style="flex:1;width:100%;background:var(--orange);display:flex;flex-direction:column;align-items:center">
      <div class="date date--card">
        <div class="date-label">Date on</div>
        <div class="date-range">AUGUST 8TH - 11TH 2019</div>
        <div class="date-time">Start time <strong>7:00PM</strong></div>
      </div>
      <div class="venue venue--light">
        <div class="venue-label">Location at</div>
        <div class="venue-text">Talbot Community Center<br>(Downtown Portland) 482 Wexley Street,<br>Portland, ME 04109</div>
      </div>
      <div class="contacts contacts--dark">
        <span class="contact"><span class="contact-icon"></span>www.vostel.org</span>
        <span class="contact"><span class="contact-icon"></span>207 555 3184</span>
        <span class="contact"><span class="contact-icon"></span>contact@meadowcrest.org</span>
      </div>
    </div>
  </section>

  <section class="flyer flyer--three">
    <div class="brand brand--top">
      <span class="brand-name"><span class="brand-dot"></span>HALSUM</span>
      <span class="brand-year">2019</span>
    </div>
    <div class="title title--white">
      <span class="title-lead">Harvest</span>
      <span class="title-main">Lantern</span>
      <span class="title-tail">Summit</span>
    </div>
    <div class="vision vision--dark">PROPHETIC | FIRE | OVERFLOW</div>
    <div class="date date--card">
      <div class="date-label">Date on</div>
      <div class="date-range">AUGUST 8TH - 11TH 2019</div>
      <div class="date-time">Start time <strong>7:00PM</strong></div>
    </div>
    <div class="venue venue--light">
      <div class="venue-label">Location at</div>
      <div class="venue-text">Talbot Community Center<br>(Downtown Portland) 482 Wexley Street,<br>Portland, ME 04109</div>
    </div>
    <div class="contacts contacts--dark">
      <span class="contact"><span class="contact-icon"></span>www.vostel.org</span>
      <span class="contact"><span class="contact-icon"></span>207 555 3184</span>
      <span class="contact"><span class="contact-icon"></span>contact@meadowcrest.org</span>
    </div>
  </section>

  <section class="flyer flyer--four">
    <div class="brand brand--top">
      <span class="brand-name"><span class="brand-dot"></span>HALSUM</span>
      <span class="brand-year">2019</span>
    </div>
    <div class="title title--white">
      <span class="title-lead">Harvest</span>
      <span class="title-main">Lantern</span>
      <span class="title-tail">Summit</span>
    </div>
    <div class="vision vision--dark">PROPHETIC | FIRE | OVERFLOW</div>
    <div class="date date--card">
      <div class="date-label">Date on</div>
      <div class="date-range">AUGUST 8TH - 11TH 2019</div>
      <div class="date-time">Start time <strong>7:00PM</strong></div>
    </div>
    <div class="venue venue--light">
      <div class="venue-label">Location at</div>
      <div class="venue-text">Talbot Community Center<br>(Downtown Portland) 482 Wexley Street,<br>Portland, ME 04109</div>
    </div>
    <div class="contacts contacts--dark">
      <span class="contact"><span class="contact-icon"></span>www.vostel.org</span>
      <span class="contact"><span class="contact-icon"></span>207 555 3184</span>
      <span class="contact"><span class="contact-icon"></span>contact@meadowcrest.org</span>
    </div>
  </section>

  <span class="sample-label" style="left:52px;top:556px">Sample1</span>
  <span class="sample-label" style="left:766px;top:556px">Sample2</span>
  <span class="sample-label" style="left:52px;top:1126px">Sample3</span>
  <span class="sample-label" style="left:766px;top:1126px">Sample4</span>
  <div class="sheet-caption">Harvest Lantern Summit 2019</div>
</main>
</body>
</html>
```